T&R Custom Homes and Remodeling Flyer

We need a new double sided flyer that showcases our service.
Our website is http://trhomesbuildco.example/
Please use the information on http://trhomesbuildco.example/about-us/ for the information in the flyer.
This handout will be used to give to our potential customers and needs to show the complete story of who we are and the services we provide. I have also attached pictures of project we have completed that should be used for the flyer.
Any other pictures can be taken from our photo gallery on the website.

Target Market(s)

Clients who want a custom home or remodel

Industry/Entity Type

Construction

Font styles to use
Serif

Requirements
Must have
• Prominent logo
• Pictures of completed projects
• Tri-fold design- eps file is attached for this
Nice to have
• Manly colors
• If you can find a tasteful way to add the picture of the owners that is great, but it should be small and is not necessary.
Should not have
• Pink/girly touches

```html
<!DOCTYPE html>
<html lang="en">
<head>
<meta charset="utf-8">
<title>T&amp;R Custom Homes and Remodeling – Tri-fold Flyer</title>
<link href="https://fonts.googleapis.com/css2?family=Oswald:wght@500;600&family=Arimo:ital,wght@0,400;0,700;1,400&display=swap" rel="stylesheet">
<style>
  :root{
    --orange:#e8682a;
    --charcoal:#3b3b3b;
    --grey-band:#dcdcdc;
    --ink:#2b2b2b;
    --paper:#ffffff;
    --bg:#e9e9e9;
  }
  *{box-sizing:border-box;margin:0;padding:0}
  html,body{width:1200px;height:1200px;overflow:hidden;background:var(--bg)}
  body{font-family:"Arimo",Arial,sans-serif;color:var(--ink);position:relative}
  .spread{position:absolute;left:60px;width:1080px;height:540px;background:var(--paper);overflow:hidden;box-shadow:0 2px 10px rgba(0,0,0,.18)}
  .spread--outside{top:40px}
  .spread--inside{top:620px}
  .fold{position:absolute;top:0;bottom:0;width:1px;background:rgba(0,0,0,.08);z-index:5}
  .fold--a{left:360px}.fold--b{left:720px}
  .block{position:absolute}
  .photo{position:absolute}
  h2.heading{font-family:"Oswald",sans-serif;font-weight:600;text-transform:uppercase;letter-spacing:.5px}
  .company-name{font-family:"Arimo",Arial,sans-serif;font-weight:700;color:var(--charcoal);text-align:center;line-height:1.25}

  /* outside – testimonials panel */
  .testimonials-photo{left:0;top:0;width:360px;height:200px;background:linear-gradient(135deg,#8e3a28 0%,#a8584a 40%,#d9cfbf 70%,#6b6457 100%)}
  .testimonials{left:0;top:180px;width:360px;height:360px;background:var(--paper);clip-path:polygon(0 30px,360px 0,360px 360px,0 360px);padding:40px 24px 16px}
  .testimonials h2{font-size:22px;color:var(--charcoal);border-bottom:1.5px solid var(--charcoal);display:inline-block;margin-bottom:10px}
  .quote{font-style:italic;font-size:9.3px;line-height:1.32;margin-bottom:9px}
  .quote cite{display:block;text-align:right;font-style:italic;font-weight:700;margin-top:2px}

  /* outside – middle panel */
  .family-photo{left:360px;top:0;width:360px;height:200px;background:linear-gradient(160deg,#7a2f22 0%,#b36049 45%,#e8e2d4 75%,#9a948a 100%)}
  .welcome{left:360px;top:180px;width:360px;height:230px;background:var(--grey-band);clip-path:polygon(0 20px,360px 0,360px 230px,0 210px);padding:40px 34px 0;text-align:center}
  .welcome .company-name{font-size:14px;margin-bottom:12px}
  .welcome p{font-size:9.3px;line-height:1.35}
  .contact{left:360px;top:390px;width:360px;height:150px;background:var(--orange);clip-path:polygon(0 20px,360px 0,360px 150px,0 150px);color:#fff;padding:26px 40px 0}
  .contact h2{font-size:22px;border-bottom:1.5px solid #fff;display:inline-block;margin-bottom:5px}
  .contact .company{font-size:12px;font-weight:700;margin-bottom:3px}
  .contact ul{list-style:none;font-size:9.5px;line-height:1.4}
  .contact li{display:flex;align-items:flex-start;gap:6px}
  .contact svg{flex:none;margin-top:2px}

  /* outside – cover panel */
  .cover-top{left:720px;top:0;width:360px;height:170px;background:var(--paper);display:flex;align-items:center;justify-content:center;padding:0 70px 0 30px}
  .cover-top .company-name{font-size:24px}
  .cover-stripe{left:1030px;top:0;width:50px;height:130px;background:var(--orange)}
  .stone-photo{left:720px;top:170px;width:360px;height:315px;background:linear-gradient(150deg,#6c5a4c 0%,#9c9286 40%,#c9c4bb 60%,#54504a 100%)}
  .phone-bar{left:720px;top:485px;width:360px;height:55px;background:var(--charcoal);color:#fff;display:flex;align-items:center;justify-content:center;gap:12px;font-size:26px;font-weight:700}

  /* inside – about */
  .owners-photo{left:0;top:0;width:360px;height:210px;background:linear-gradient(180deg,#e7e2d8 0%,#cfc7b8 55%,#2a2a2a 100%)}
  .about{left:0;top:195px;width:360px;height:345px;background:var(--paper);clip-path:polygon(0 20px,360px 0,360px 345px,0 345px);padding:28px 22px 10px}
  .about h2{font-size:20px;color:var(--charcoal);border-bottom:1.5px solid var(--charcoal);display:inline-block;margin:0 0 6px 90px}
  .about p{font-size:8.6px;line-height:1.27;margin-bottom:5px}
  .about .signatures{font-size:9.5px;font-style:italic;font-weight:700;line-height:1.3}
  .about .mini-mark{position:absolute;right:22px;bottom:16px;font-size:10px}

  /* inside – gallery and services */
  .bar-photo{left:360px;top:0;width:170px;height:260px;background:linear-gradient(170deg,#2d2f35 0%,#6a5a4a 55%,#8c3a2c 100%)}
  .after-photo{left:530px;top:0;width:190px;height:130px;background:linear-gradient(150deg,#7a6a5a,#b3ab9f 55%,#595450)}
  .before-photo{left:530px;top:130px;width:190px;height:130px;background:linear-gradient(150deg,#9a9690,#cfcac2 55%,#6d6a66)}
  .tag{position:absolute;right:8px;bottom:6px;font-family:"Oswald",sans-serif;font-size:10px;color:#fff;font-weight:600}
  .hall-photo{left:720px;top:0;width:360px;height:120px;background:linear-gradient(180deg,#efe8dc 0%,#d7cbb7 60%,#3d2a20 100%)}
  .cabinet-photo{left:720px;top:120px;width:180px;height:90px;background:linear-gradient(160deg,#2a63a8,#3c2c24)}
  .vanity-photo{left:900px;top:120px;width:180px;height:90px;background:linear-gradient(160deg,#4a352a,#8a7766)}
  .wood-photo{left:720px;top:210px;width:180px;height:90px;background:linear-gradient(160deg,#7a3f1f,#b5733f)}
  .tile-photo{left:900px;top:210px;width:180px;height:90px;background:linear-gradient(160deg,#5d5a56,#2f2b28)}
  .kitchen-photo{left:360px;top:300px;width:720px;height:240px;background:linear-gradient(170deg,#4a3428 0%,#d9d2c5 45%,#f1ede6 70%,#3a2a22 100%);clip-path:polygon(360px 0,720px 0,720px 240px,0 240px,0 140px,360px 140px)}
  .services{left:360px;top:250px;width:360px;height:190px;background:var(--orange);color:#fff;padding:20px 26px 0;clip-path:polygon(0 10px,360px 0,360px 190px,0 190px)}
  .services h2{font-size:24px;border-bottom:1.5px solid #fff;display:inline-block;margin:0 0 8px 70px}
  .services ul{list-style:none;font-size:11px;font-weight:700;text-transform:uppercase;line-height:1.6;margin-bottom:6px}
  .services li{display:flex;align-items:center;gap:8px}
  .services p{font-size:9.5px;line-height:1.35}
</style>
</head>
<body>

<section class="spread spread--outside" aria-label="Flyer outside">
  <div class="fold fold--a"></div><div class="fold fold--b"></div>

  <div class="photo testimonials-photo" role="img" aria-label="Photo of a brick home exterior with a white porch railing"></div>
  <div class="block testimonials">
    <h2 class="heading">Testimonials</h2>
    <p class="quote">“We had our basement finished by T&amp;R Custom Homes &amp; Remodeling last year, and although they came highly recommended, the work that they did exceeded all our expectations. Not only was there an incredible attention to detail, but the courtesy and service we received was superior. The basement looks fabulous and we couldn't be happier.”<cite>- The Marlows, Eastbrook IL</cite></p>
    <p class="quote">We were very skeptical given our previous dealings; however, that feeling quickly subsided given T&amp;R's approach to putting their customers first, their billing transparency and how every detail matters to them in the building process. I can honestly say that you cannot go wrong if you decided to build your custom dream home with T&amp;R Homes!<cite>- Dan &amp; Erin Holt, Westmoor IL</cite></p>
    <p class="quote">“Six months ago we finished our basement and having T&amp;R Custom Homes &amp; Remodeling complete the job was one of the best decisions we had made during that process. From the initial consultation to the final walk through, Ray listened to what we wanted, offered suggestions when we needed it and provided us with a professional insight that we could not have done without. Our basement is not just a finished basement but an addition to our existing living space.”<cite>- Mark &amp; Lisa Brenner, Westmoor IL</cite></p>
  </div>

  <div class="photo family-photo" role="img" aria-label="Photo of homeowners seated on the front steps of their brick home"></div>
  <div class="block welcome">
    <div class="company-name">T&amp;R Custom Homes and Remodeling</div>
    <p>Welcome to T&amp;R Custom Homes &amp; Remodeling, LLC serving the Chicago suburban area. The quality of T&amp;R shows in every detail. Our services range from new construction, to kitchen, bathroom and basement remodeling and everything in-between. T&amp;R approaches every project with an eye for detail and quality using exceptional craftsmanship combined with years of experience.</p>
  </div>
  <div class="block contact">
    <h2 class="heading">Contact Us</h2>
    <div class="company">T &amp; R Homes LLC</div>
    <ul>
      <li><svg width="8" height="10" viewBox="0 0 8 10"><path d="M4 0a3.5 3.5 0 0 0-3.5 3.5C.5 6 4 10 4 10s3.5-4 3.5-6.5A3.5 3.5 0 0 0 4 0zm0 5a1.4 1.4 0 1 1 0-2.8A1.4 1.4 0 0 1 4 5z" fill="#fff"/></svg>4100 Harmon Road Suite 210<br>Fairhaven, IL 60000, USA</li>
      <li><svg width="9" height="9" viewBox="0 0 24 24"><path d="M6.6 10.8a15 15 0 0 0 6.6 6.6l2.2-2.2a1 1 0 0 1 1-.25 11.4 11.4 0 0 0 3.6.57 1 1 0 0 1 1 1V20a1 1 0 0 1-1 1A17 17 0 0 1 3 4a1 1 0 0 1 1-1h3.5a1 1 0 0 1 1 1c0 1.25.2 2.45.57 3.57a1 1 0 0 1-.25 1z" fill="#fff"/></svg>555-014-2270</li>
      <li><svg width="9" height="9" viewBox="0 0 10 10"><circle cx="5" cy="5" r="4.2" fill="none" stroke="#fff" stroke-width="1.2"/><path d="M.8 5h8.4M5 .8c2 2.4 2 6 0 8.4M5 .8c-2 2.4-2 6 0 8.4" fill="none" stroke="#fff" stroke-width=".8"/></svg>www.trhomesbuildco.example</li>
    </ul>
  </div>

  <div class="block cover-top">
    <div class="company-name">T&amp;R Custom Homes and Remodeling</div>
  </div>
  <div class="block cover-stripe"></div>
  <div class="photo stone-photo" role="img" aria-label="Photo of a stone-and-brick home entrance with white columns"></div>
  <div class="block phone-bar">
    <svg width="26" height="26" viewBox="0 0 26 26"><circle cx="13" cy="13" r="11.5" fill="none" stroke="#fff" stroke-width="1.8"/><path d="M9.3 11.6a9 9 0 0 0 5.1 5.1l1.4-1.4a.7.7 0 0 1 .7-.16 7 7 0 0 0 2.2.35.6.6 0 0 1 .6.6v2.2a.6.6 0 0 1-.6.6A10.4 10.4 0 0 1 8.3 8.5a.6.6 0 0 1 .6-.6h2.2a.6.6 0 0 1 .6.6c0 .77.12 1.5.35 2.2a.7.7 0 0 1-.16.7z" fill="#fff"/></svg>
    <span>(555) 014-2270</span>
  </div>
</section>

<section class="spread spread--inside" aria-label="Flyer inside">
  <div class="fold fold--a"></div><div class="fold fold--b"></div>

  <div class="photo owners-photo" role="img" aria-label="Photo of the two company partners in black polo shirts"></div>
  <div class="block about">
    <h2 class="heading">About Us</h2>
    <p>With more than 20 years combined experience in construction, T&amp;R maintains the absolute highest levels of quality, material, workmanship, and service in each and every project we build.</p>
    <p>A reputation is only as great as the last referral and we understand that the future of our business relies upon satisfied customers. We take the time to fully understand our customer's expectations. Customer service is more than just a trendy marketing theme, it is the underlying philosophy in everything we do and our home buyers reap the benefits of this philosophy.</p>
    <p>T&amp;R is committed to building quality homes with meticulous craftsmanship, custom designs, and thoughtful touches that add to the homeowners' quality of life. Over the years, we have developed close working relationships with some of the best local craftsmen, vendors, and suppliers located in the western suburbs of Chicago.</p>
    <p>These trade partners know we expect only the highest level of craftsmanship and they are required to perform at only the highest standards of professionalism, accuracy and timeliness. We take pride in creating homes that are as beautiful to look at, as they are comfortable to live in.</p>
    <p>Throughout our experience we have developed lasting values of honesty, real quality, attention to fine detail, efficiency, timeliness, and most of all how to meet a customers expectation by asking the right questions. With these principles, character and dedication we are able to do things right the first time.</p>
    <div class="signatures">Tom Rinaldi- Partner<br>Ray Costa- Partner</div>
    <div class="company-name mini-mark">T&amp;R Custom Homes</div>
  </div>

  <div class="photo bar-photo" role="img" aria-label="Photo of a finished kitchen island with bar stools and pendant lights"></div>
  <div class="photo after-photo" role="img" aria-label="Photo of a renovated home entrance, after"><span class="tag">AFTER</span></div>
  <div class="photo before-photo" role="img" aria-label="Photo of the home entrance before renovation"><span class="tag">BEFORE</span></div>
  <div class="photo hall-photo" role="img" aria-label="Photo of a bright entry hall with a chandelier and arched doorway"></div>
  <div class="photo cabinet-photo" role="img" aria-label="Photo of a room with a blue accent wall"></div>
  <div class="photo vanity-photo" role="img" aria-label="Photo of dark wood bathroom cabinets"></div>
  <div class="photo wood-photo" role="img" aria-label="Photo of warm wood kitchen cabinetry"></div>
  <div class="photo tile-photo" role="img" aria-label="Photo of a mosaic tile backsplash and dark counter"></div>
  <div class="photo kitchen-photo" role="img" aria-label="Photo of a large kitchen with white cabinets and dark wood floors"></div>

  <div class="block services">
    <h2 class="heading">Our Services</h2>
    <ul>
      <li><svg width="12" height="12" viewBox="0 0 12 12"><circle cx="6" cy="6" r="6" fill="#fff"/><path d="M3.2 6.2 5.2 8l3.6-4" fill="none" stroke="#e8682a" stroke-width="1.6"/></svg>Construction ( All Types )</li>
      <li><svg width="12" height="12" viewBox="0 0 12 12"><circle cx="6" cy="6" r="6" fill="#fff"/><path d="M3.2 6.2 5.2 8l3.6-4" fill="none" stroke="#e8682a" stroke-width="1.6"/></svg>Remodeling</li>
      <li><svg width="12" height="12" viewBox="0 0 12 12"><circle cx="6" cy="6" r="6" fill="#fff"/><path d="M3.2 6.2 5.2 8l3.6-4" fill="none" stroke="#e8682a" stroke-width="1.6"/></svg>Building-Related Services</li>
    </ul>
    <p>Let T&amp;R Homes be a part of your next construction project...you'll be happy that you did.</p>
    <p>Whether the job is big or small, T&amp;R promise one-on-one service with customer satisfaction guaranteed.</p>
  </div>
</section>

</body>
</html>
```